Mobile Responsive design for a promotional products company shopping cart

before participating on the contest i would want you first understand my requirements..read through, understand, think if you can create the best design and then get involved on my project.

this is an website selling promotional products, branded merchandise for corporates and end users. in simple a website selling corporate gifts

Need both online selling & enquiry mode

need the best user experience from homepage, category view, product view, admin, inventory management and mobile responsive page.

show me the best ui and ux.

please research on the website before creating this design. i want the website to be competitive like giftvantaro.com.au

Target Market(s)

corporate gifts, promotional products, branded merchandise - AU market

Industry/Entity Type

It Company

Number of Pages Required

4 page

Requirements
Must have
• bright colours
• unique designs
• good user experience
• must show me
• homepage
• category page
• product details page
• admin+inventory
• mobile responsive design

```html
<!DOCTYPE html>
<html lang="en">
<head>
<meta charset="utf-8">
<title>Brightpeak Promotional Products</title>
<link rel="stylesheet" href="https://fonts.googleapis.com/css2?family=Open+Sans:wght@400;600;700&family=Raleway:wght@400;500;600;700&display=swap">
<style>
:root{
  --orange:#f7931e;
  --orange-dark:#e9801a;
  --blue:#2b8fd0;
  --nav:#2f86cf;
  --nav-deep:#1d6db5;
  --ink:#333;
  --muted:#777;
  --grey-bg:#f1f1f1;
  --footer:#4b4b4b;
  --footer-deep:#3a3a3a;
  --t-blue:#4a7fcf;--t-red:#d9605a;--t-green:#3cb878;--t-purple:#9b6aa8;
  --t-orange:#ef8e3f;--t-pink:#e07cbf;--t-yellow:#e3c13f;--t-teal:#6cc3d3;
}
*{box-sizing:border-box;margin:0;padding:0}
html,body{width:1200px;height:2773px;overflow:hidden}
body{position:relative;font-family:"Open Sans",sans-serif;color:var(--ink);background:#fff;font-size:13px}
.abs{position:absolute}

.topbar{left:0;top:0;width:1200px;height:37px;background:var(--orange)}
.topbar ul{list-style:none;position:absolute;left:530px;top:0;display:flex;height:37px}
.topbar li{color:#fff;font-size:13px;line-height:37px;padding:0 36px;border-left:1px solid rgba(255,255,255,.35)}
.topbar li:first-child{border:0;padding-left:10px}

.header{left:0;top:37px;width:1200px;height:180px;background:linear-gradient(#fde7cf,#fff)}
.logo{left:100px;top:80px;display:flex;align-items:center;gap:10px}
.logo span{font-family:"Raleway",sans-serif;font-weight:700;font-size:34px;color:var(--blue)}
.logo i{width:14px;height:14px;border-radius:50%;background:var(--orange)}
.search{left:368px;top:85px;width:257px;height:30px;display:flex;background:#fff;border:1px solid #ddd}
.search .sel{width:44px;background:#e6e6e6;font-size:11px;line-height:28px;text-align:center;color:#666}
.search .in{flex:1;font-size:11px;color:#999;line-height:28px;padding-left:8px}
.search .btn{width:26px;background:var(--orange)}
.guarantee{left:669px;top:86px;display:flex;align-items:center;gap:10px;font-size:13px;color:#444}
.ring{width:28px;height:28px;border-radius:50%;border:3px solid var(--orange)}
.phone{left:937px;top:80px}
.phone .num{position:absolute;left:42px;top:0;font-size:22px;color:var(--blue);white-space:nowrap}
.phone .note{position:absolute;left:20px;top:40px;font-size:12px;color:#666;white-space:nowrap}

.nav{left:100px;top:161px;width:1000px;height:35px;background:var(--nav);display:flex;align-items:center;color:#fff;font-size:14px}
.nav .cat{background:var(--nav-deep);height:35px;display:flex;align-items:center;gap:10px;padding:0 18px 0 10px;font-weight:700;font-size:13px}
.nav a{color:#fff;text-decoration:none;margin-left:32px}
.nav a.home{font-weight:700;font-size:15px;margin-left:20px}
.nav .lang{margin-left:auto;margin-right:12px;font-size:10px;background:var(--nav-deep);padding:3px 8px}

.hero{left:100px;top:211px;width:1000px;height:384px;box-shadow:0 26px 22px -20px rgba(0,0,0,.35)}
.hero .photo{position:absolute;left:0;top:0;width:604px;height:384px;background:linear-gradient(120deg,#8a8e92,#c9ccce 45%,#6f7378)}
.hero .panel{position:absolute;left:604px;top:0;width:396px;height:384px;background:linear-gradient(160deg,#3b3d40,#222)}
.hero h1{position:absolute;left:55px;top:133px;font-family:"Raleway",sans-serif;font-weight:600;font-size:22px;color:#fff;white-space:nowrap}
.hero .hs{position:absolute;left:55px;top:177px;width:457px;height:41px;display:flex}
.hero .hs div{flex:1;background:#fff;font-size:13px;color:#aaa;line-height:41px;padding-left:18px}
.hero .hs b{width:42px;background:var(--orange)}
.hero .browse{position:absolute;left:370px;top:223px;background:#fff;color:var(--blue);font-size:10px;padding:4px 8px}
.dots{position:absolute;left:58px;top:350px;display:flex;gap:12px}
.dots i{width:14px;height:14px;border-radius:50%;background:#fff}
.dots i:first-child{background:var(--orange)}
.feat{position:absolute;left:34px;display:flex;gap:16px;align-items:center}
.feat .c{width:82px;height:82px;border-radius:50%;background:#fff;flex:none;display:flex;align-items:center;justify-content:center}
.feat .c.o{background:var(--orange);border:4px solid #fff}
.feat b{display:block;color:var(--orange);font-size:15px;font-weight:600;margin-bottom:8px}
.feat p{color:#fff;font-size:12px;line-height:22px;width:240px}

.lead{left:0;top:646px;width:1200px;text-align:center;font-family:"Raleway",sans-serif;font-weight:500;font-size:26px;color:var(--orange)}
.intro{left:180px;top:690px;width:840px;text-align:center;font-size:12px;line-height:22px;color:#555}

.tile{width:244px;height:167px;color:#fff;text-align:center;font-size:17px}
.tile svg{position:absolute;left:82px;top:40px}
.tile span{position:absolute;left:0;bottom:16px;width:100%}

.featured{left:0;top:1183px;width:1200px;height:444px;background:var(--grey-bg)}
.sec-title{width:1200px;left:0;text-align:center;font-family:"Raleway",sans-serif;font-weight:500;font-size:26px;color:var(--orange)}
.card{top:1268px;width:243px;height:309px;background:#fff;border:1px solid #ddd}
.card .img{position:absolute;left:20px;top:10px;width:201px;height:180px}
.card .name{position:absolute;top:200px;width:100%;text-align:center;font-size:17px;color:#333}
.card .desc{position:absolute;top:224px;width:100%;text-align:center;font-size:11px;color:#555}
.card .price{position:absolute;left:26px;top:256px;font-size:19px;color:#e0503a}
.card .add{position:absolute;right:20px;top:258px;width:97px;height:28px;background:var(--orange-dark);color:#fff;font-size:11px;text-align:center;line-height:28px;border-radius:2px}
.arrow{top:1398px}

.banner{top:1679px;height:288px;border:8px solid #fff;box-shadow:0 0 0 1px #e5e5e5}
.banner h2{position:absolute;left:58px;top:72px;font-family:"Raleway",sans-serif;font-weight:700;font-size:24px;color:#fff}
.banner p{position:absolute;left:58px;top:110px;width:390px;color:#fff;font-size:13px;line-height:22px}

.t-avatar{width:106px;height:106px;border-radius:50%;border:3px solid #ddd;background:linear-gradient(#c9d3dc,#8a99a8)}
.t-text{width:252px;font-size:12px;line-height:22px;text-align:justify;color:#555}
.t-name{font-size:15px;color:var(--blue);font-weight:600}
.t-role{font-size:11px;color:#999}
.t-meta{display:flex;gap:6px;align-items:center;font-size:9px;color:#999}
.stars{color:#f2b01e;font-size:13px;letter-spacing:1px}
.circ{width:38px;height:38px;border-radius:50%;background:#e3e3e3;display:flex;align-items:center;justify-content:center}

.trusted{left:0;top:2315px;width:1200px;height:120px;background:#f3f3f3}
.trusted .lbl{position:absolute;left:100px;top:46px;font-size:19px;color:#333}
.brands{position:absolute;left:213px;top:20px;width:776px;height:78px;background:#fff;border:1px solid #ddd;display:flex;align-items:center;justify-content:space-around}
.brands span{font-weight:700;font-size:26px;color:#555}
.sq{width:20px;height:20px;background:#aaa}

.footer{left:0;top:2435px;width:1200px;height:270px;background:var(--footer);color:#eee}
.fcol{position:absolute;top:64px}
.fcol h3{font-family:"Raleway",sans-serif;font-weight:600;font-size:18px;color:#fff;margin-bottom:8px}
.fcol li{list-style:none;font-size:12px;line-height:26px;color:#ddd}
.fcol p{font-size:12px;color:#ddd}
.email{width:273px;height:33px;background:#fff;color:#888;font-size:11px;line-height:33px;padding-left:14px;margin-top:8px}
.sub{width:116px;height:34px;background:var(--orange);color:#fff;font-weight:700;font-size:13px;line-height:34px;text-align:center;margin-top:9px}
.bottom{left:0;top:2705px;width:1200px;height:68px;background:var(--footer-deep);color:#eee;font-size:12px}
.bottom p{position:absolute;left:142px;top:26px}
.social{position:absolute;left:967px;top:20px;display:flex;gap:7px}
.social i{width:24px;height:24px;background:#fff;border-radius:3px}
</style>
</head>
<body>

<div class="abs topbar"><ul><li>&#128722; CART (0)</li><li>My Account</li><li>Wish List</li><li>Login</li><li>Sign Up</li></ul></div>

<header class="abs header"></header>
<div class="abs logo"><span>Brightpeak</span><i></i></div>
<div class="abs search"><div class="sel">All ▾</div><div class="in">Search entire catalogue here</div><div class="btn"></div></div>
<div class="abs guarantee"><div class="ring"></div>100 % satisfaction guaranteed</div>
<div class="abs phone">
  <svg width="34" height="34" viewBox="0 0 34 34"><circle cx="17" cy="17" r="15" fill="none" stroke="#f7931e" stroke-width="3"/><path d="M12 10c1-1 2-1 3 0l1 3c0 1-1 2-1 2 1 2 3 4 5 5 0 0 1-1 2-1l3 1c1 1 1 2 0 3-2 2-5 2-8-1s-6-6-6-9c0-1 0-2 1-3z" fill="#f7931e"/></svg>
  <div class="num">1300 555 018</div>
  <div class="note">Nationwide local call</div>
</div>

<nav class="abs nav">
  <div class="cat"><svg width="14" height="12"><rect width="14" height="2" fill="#fff"/><rect y="5" width="14" height="2" fill="#fff"/><rect y="10" width="14" height="2" fill="#fff"/></svg>CATEGORIES</div>
  <a class="home">Home</a><a>Latest Products</a><a>Express Items</a><a>What Our Clients Say</a><a>Newsletter Signup</a>
  <span class="lang">ENGLISH ▾</span>
</nav>

<section class="abs hero">
  <div class="photo" role="img" aria-label="Desk workspace with tablets, notebook and pens"></div>
  <div class="panel">
    <div class="feat" style="top:24px"><div class="c"><svg width="40" height="34"><rect x="4" y="4" width="32" height="20" fill="none" stroke="#2b8fd0" stroke-width="3"/><rect x="16" y="24" width="8" height="6" fill="#2b8fd0"/></svg></div><div><b>Free design assistance</b><p>visual mock ups / Pre production samples</p></div></div>
    <div class="feat" style="top:144px"><div class="c o"><svg width="30" height="30"><circle cx="15" cy="15" r="12" fill="#fff"/><text x="15" y="20" font-size="14" text-anchor="middle" fill="#f7931e" font-family="Open Sans">%</text></svg></div><div><b>Best Prices Guarantee</b><p>Challenge us to beat any written quote</p></div></div>
    <div class="feat" style="top:268px"><div class="c"><svg width="40" height="40"><circle cx="18" cy="15" r="6" fill="#2b8fd0"/><path d="M6 36c0-8 6-13 12-13s12 5 12 13z" fill="#2b8fd0"/><rect x="24" y="2" width="14" height="9" rx="2" fill="#2b8fd0"/></svg></div><div><b>Speak with our team today</b><p>Free ideas &amp; Advice from our brand experts</p></div></div>
  </div>
  <h1>TRUST US TO DELIVER ON TIME, EVERYTIME</h1>
  <div class="hs"><div>Search 1000's of promotional products</div><b></b></div>
  <div class="browse">BROWSE ALL PRODUCTS</div>
  <div class="dots"><i></i><i></i><i></i></div>
</section>

<h2 class="abs lead">Australia's Leading Promotional Product Supplier</h2>
<p class="abs intro">Lorem Ipsum is simply dummy text of the printing and typesetting industry. Lorem Ipsum has been the industry's standard dummy text ever since the 1500s, when an unknown printer took a galley of type and scrambled it to make a type specimen book. It has survived not only five centuries, but also the leap into electronic typesetting, remaining essentially unchanged. I</p>

<div class="abs tile" style="left:100px;top:777px;background:var(--t-blue)"><svg width="80" height="80"><path d="M16 30h48l-4 42H20z" fill="#fff"/><path d="M28 30v-8a12 12 0 0 1 24 0v8" fill="none" stroke="#fff" stroke-width="4"/></svg><span>Bags</span></div>
<div class="abs tile" style="left:351px;top:777px;background:var(--t-red)"><svg width="80" height="80"><rect x="30" y="14" width="22" height="56" rx="6" fill="#fff" transform="rotate(35 40 42)"/></svg><span>Drink Botttles</span></div>
<div class="abs tile" style="left:605px;top:777px;background:var(--t-green)"><svg width="80" height="80"><rect x="28" y="14" width="22" height="50" rx="6" fill="#fff" transform="rotate(45 40 40)"/></svg><span>Usb Drives</span></div>
<div class="abs tile" style="left:858px;top:777px;background:var(--t-purple)"><svg width="80" height="80"><path d="M20 64l6-18 30-30 12 12-30 30z" fill="#fff"/><path d="M14 72h40" stroke="#fff" stroke-width="3"/></svg><span>Pens</span></div>
<div class="abs tile" style="left:100px;top:956px;background:var(--t-orange)"><svg width="80" height="80"><path d="M14 52a26 24 0 0 1 52 0z" fill="#fff"/><path d="M10 54h64l-6 8H10z" fill="#fff"/></svg><span>Cap &amp; Hats</span></div>
<div class="abs tile" style="left:351px;top:956px;background:var(--t-pink)"><svg width="80" height="80"><path d="M4 40a36 30 0 0 1 72 0z" fill="#fff"/><path d="M40 40v24a5 5 0 0 1-10 0" fill="none" stroke="#fff" stroke-width="4"/></svg><span>Umbrella</span></div>
<div class="abs tile" style="left:605px;top:956px;background:var(--t-yellow)"><svg width="80" height="80"><path d="M28 12l-18 10 6 14 8-4v36h32V32l8 4 6-14-18-10c-2 6-6 8-12 8s-10-2-12-8z" fill="#fff"/></svg><span>T-shirts</span></div>
<div class="abs tile" style="left:858px;top:956px;background:var(--t-teal)"><svg width="80" height="80"><rect x="22" y="36" width="36" height="36" fill="#fff"/><rect x="28" y="10" width="5" height="28" fill="#fff"/><rect x="38" y="14" width="5" height="24" fill="#fff"/><rect x="48" y="8" width="5" height="30" fill="#fff"/></svg><span>Stubby Holders</span></div>

<section class="abs featured"></section>
<h2 class="abs sec-title" style="top:1206px">Featured Promo Products</h2>
<svg class="abs arrow" style="left:33px" width="18" height="48"><path d="M14 2L4 24l10 22" fill="none" stroke="#bbb" stroke-width="2"/></svg>
<svg class="abs arrow" style="left:1140px" width="18" height="48"><path d="M4 2l10 22L4 46" fill="none" stroke="#bbb" stroke-width="2"/></svg>

<div class="abs card" style="left:98px"><div class="img" role="img" aria-label="Green and natural tote bags" style="background:linear-gradient(#f4f7ef,#d9e8c9)"></div><div class="name">Product Name</div><div class="desc">Morbi diam mauris viverra in gravid</div><div class="price">$57.58</div><div class="add">Add to Cart</div></div>
<div class="abs card" style="left:351px"><div class="img" role="img" aria-label="White cosmetic bottle" style="background:linear-gradient(#fafafa,#e3e8ee)"></div><div class="name">Product Name</div><div class="desc">Morbi diam mauris viverra in gravid</div><div class="price">$57.58</div><div class="add">Add to Cart</div></div>
<div class="abs card" style="left:605px"><div class="img" role="img" aria-label="Green plastic measuring cup" style="background:linear-gradient(#f6faf4,#d7ecd0)"></div><div class="name">Product Name</div><div class="desc">Morbi diam mauris viverra in gravid</div><div class="price">$57.58</div><div class="add">Add to Cart</div></div>
<div class="abs card" style="left:860px"><div class="img" role="img" aria-label="Yellow dispenser bottle" style="background:linear-gradient(#fcfaf1,#f1e4b6)"></div><div class="name">Product Name</div><div class="desc">Morbi diam mauris viverra in gravid</div><div class="price">$57.58</div><div class="add">Add to Cart</div></div>

<div class="abs banner" style="left:118px;width:470px;background:linear-gradient(120deg,#2a3346,#5a4c5c 60%,#b98a60)" role="img" aria-label="Colour print proofs on a press table">
  <h2>HIGH QUALITY PRINTING</h2>
  <p>Whether you need caps embroidered with your logo, t-shirt screen printed or your brand laser engraved on pens, our team has an expert knowledge of printing techniques across multiple supports.</p>
</div>
<div class="abs banner" style="left:610px;width:472px;background:linear-gradient(135deg,#e8e8e8,#9a9a9a 45%,#2a2a2a)" role="img" aria-label="Branded wall clock and merchandise mockup"></div>

<h2 class="abs sec-title" style="top:2014px">What Our Clients Say</h2>
<div class="abs t-avatar" style="left:166px;top:2066px" role="img" aria-label="Client portrait"></div>
<p class="abs t-text" style="left:303px;top:2064px">Lorem Ipsum is simply dummy text of the printing and typesetting industry. Lorem Ipsum has been the industry's standard dummy text ever since the 1500s,</p>
<div class="abs t-name" style="left:303px;top:2162px">Marla Venn,</div>
<div class="abs t-role" style="left:303px;top:2186px">Financial Services Professional</div>
<div class="abs t-meta" style="left:303px;top:2210px"><span class="stars">★★★½☆</span>○ comments</div>
<div class="abs t-avatar" style="left:646px;top:2066px" role="img" aria-label="Client portrait"></div>
<p class="abs t-text" style="left:782px;top:2064px">Lorem Ipsum is simply dummy text of the printing and typesetting industry. Lorem Ipsum has been the industry's standard dummy text ever since the 1500s,</p>
<div class="abs t-name" style="left:782px;top:2162px">Tobias R. Elwin,</div>
<div class="abs t-role" style="left:782px;top:2186px">Financial Services Professional</div>
<div class="abs t-meta" style="left:782px;top:2210px"><span class="stars">★★★½☆</span>○ comments</div>
<div class="abs circ" style="left:541px;top:2220px"><svg width="12" height="14"><path d="M9 2L3 7l6 5" fill="none" stroke="#fff" stroke-width="2"/></svg></div>
<div class="abs circ" style="left:591px;top:2220px"><svg width="12" height="14"><path d="M3 2l6 5-6 5" fill="none" stroke="#fff" stroke-width="2"/></svg></div>

<section class="abs trusted">
  <span class="lbl">Trusted by</span>
  <div class="brands"><span>Norvex</span><span>Kestrel</span><span>Altura</span><span>Pimbrook</span><span>Quellon</span></div>
  <div class="abs sq" style="left:1011px;top:50px"></div>
  <div class="abs sq" style="left:1037px;top:50px"></div>
</section>

<footer class="abs footer">
  <div class="fcol" style="left:142px"><h3>COMPANY</h3><ul><li>About us</li><li>Contact Us</li><li>My account</li><li>Orders history</li><li>Advanced search</li><li>Shipping</li></ul></div>
  <div class="fcol" style="left:342px"><h3>OUR RANGE</h3><ul><li>Merchandise</li><li>Clothing</li><li>Caps &amp; Hats</li><li>Bags</li><li>Pens</li><li>Drinkware</li></ul></div>
  <div class="fcol" style="left:592px"><h3>SUPPORT</h3><ul><li>FAQs</li><li>Privacy Policy</li><li>Recommendations</li><li>Contact</li></ul></div>
  <div class="fcol" style="left:775px"><h3>NEWSLETTER SIGN UP</h3><p>Please sign up here for latest deals</p><div class="email">Email address</div><div class="sub">SUBSCRIBE</div></div>
</footer>
<div class="abs bottom"><p>© 2016 Brightpeak  All right reserved  Term of Use</p><div class="social"><i></i><i></i><i></i></div></div>

</body>
</html>
```